Cradlekin by Marianne Business Card Design

i am starting a new business as a reborn artist (that is painting dolls to make them look like real live babies)

i eventually want to sell the dolls that i make and have classed in reborning. but at the moment i just want to get my name out there.

I do not currently have images of the dolls so cannot have an image in the design.

Non compulsory thoughts: i like the look of old wood, white and baby pink,even hot pink, and lace, denim. i had in mind something like a tiny baby in a old cradle or something, a old drawer, box, something different or unusual, it has to be a girl baby. i am also open to other thoughts on the matter. i would like plain writing not all swirly
Updates

Sorry to change but would like it to read country cradlekin by marianne.

Reason: I have not been able to find the design I am looking for

Industry/Entity Type

Painting

Contact Information for Business Card

Cradlekin by Marianne
country babies that never grow up
Reborn Artist Marianne Holt
0437 651 840
lunet.v@mailvane.net

```html
<!DOCTYPE html>
<html lang="en">
<head>
<meta charset="utf-8">
<title>Cradlekin by Marianne – Business Card</title>
<link rel="stylesheet" href="https://fonts.googleapis.com/css2?family=Arimo:wght@400;700&display=swap">
<style>
  :root {
    --cream: #fbf1d6;
    --rose: #e9566f;
    --olive: #86691f;
    --white: #ffffff;
  }
  html, body {
    margin: 0;
    padding: 0;
    overflow: hidden;
    background: var(--cream);
  }
  .card {
    position: relative;
    width: 1200px;
    height: 740px;
    background: var(--cream);
    overflow: hidden;
    font-family: "Arimo", Arial, sans-serif;
  }
  .ribbon {
    position: absolute;
    left: 117px;
    top: 0;
    width: 284px;
    height: 300px;
    background: var(--rose);
  }
  .brand-seal {
    position: absolute;
    left: 72px;
    top: 183px;
    width: 374px;
    height: 374px;
    border-radius: 50%;
    background: var(--white);
    box-shadow: 0 2px 6px rgba(120, 100, 60, 0.25);
    display: flex;
    align-items: center;
    justify-content: center;
    text-align: center;
  }
  .brand-name {
    margin: 0;
    color: var(--rose);
    font-weight: 700;
    font-size: 28px;
    line-height: 1;
    white-space: nowrap;
  }
  .identity {
    position: absolute;
    left: 743px;
    top: 448px;
  }
  .person-name {
    margin: 0;
    color: var(--rose);
    font-weight: 700;
    font-size: 46px;
    line-height: 1;
    letter-spacing: 0.5px;
  }
  .person-role {
    margin: 10px 0 0 2px;
    color: var(--olive);
    font-weight: 400;
    font-size: 27px;
    letter-spacing: 1.5px;
    line-height: 1;
  }
  .divider {
    position: absolute;
    left: 655px;
    right: 0;
    top: 549px;
    height: 3px;
    border-top: 2px solid var(--olive);
    border-bottom: 2px solid var(--olive);
  }
  .contacts {
    position: absolute;
    left: 746px;
    top: 575px;
    margin: 0;
    padding: 0;
    list-style: none;
  }
  .contact-item {
    display: flex;
    align-items: center;
    height: 32px;
    color: var(--olive);
    font-size: 23px;
    letter-spacing: 0.8px;
  }
  .contact-icon {
    width: 22px;
    height: 16px;
    margin-right: 17px;
    fill: none;
    stroke: var(--olive);
  }
</style>
</head>
<body>
  <main class="card">
    <div class="ribbon"></div>
    <div class="brand-seal">
      <p class="brand-name">Cradlekin by Marianne</p>
    </div>

    <header class="identity">
      <h1 class="person-name">Marianne Holt</h1>
      <p class="person-role">REBORN ARTIST</p>
    </header>

    <div class="divider"></div>

    <ul class="contacts">
      <li class="contact-item">
        <svg class="contact-icon" viewBox="0 0 22 16" aria-hidden="true">
          <path d="M6 2 C4 2 3.5 4 4 6 C5 10 8 13 12 14 C14 14.5 15.5 13.5 15.5 12 L13 10 L11.5 11.2 C9.5 10.3 7.8 8.6 7 6.6 L8.2 5 Z" fill="var(--olive)" stroke="none"/>
        </svg>
        <span>0437 651 840</span>
      </li>
      <li class="contact-item">
        <svg class="contact-icon" viewBox="0 0 22 16" aria-hidden="true">
          <rect x="1" y="2" width="20" height="12" stroke-width="1.3"/>
          <path d="M1 2 L11 9.5 L21 2 M1 14 L8.5 7.5 M21 14 L13.5 7.5" stroke-width="1.3"/>
        </svg>
        <span>lunet.v@mailvane.net</span>
      </li>
    </ul>
  </main>
</body>
</html>
```